Accounting company website and Facebook page design

I need a website designed and copy written for an accounting/bookkeeping company in Ohio. We have content but would need someone to fine-tune it and make it sound good. I also need a Facebook page design created. Attached is the logo for the company.

```html
<!DOCTYPE html>
<html lang="en">
<head>
<meta charset="utf-8">
<title>Northfield Ledger Co. — Accounting and Bookkeeping Services</title>
<link rel="stylesheet" href="https://fonts.googleapis.com/css2?family=Cinzel:wght@400;500;600&family=Poppins:wght@300;400;500;600&display=swap">
<style>
:root{
  --gold:#e8a21c;
  --ink:#2a292e;
  --text:#4a4a4a;
  --muted:#6b6b6b;
  --panel:#f6f6f8;
  --white:#ffffff;
}
*{margin:0;padding:0;box-sizing:border-box}
html,body{width:1200px;height:3424px;overflow:hidden}
body{position:relative;background:var(--white);font-family:"Poppins",sans-serif;color:var(--text)}
h1,h2,h3,h4{font-weight:400}
.abs{position:absolute}
.btn{position:absolute;display:flex;align-items:center;justify-content:center;background:var(--gold);color:var(--white);border-radius:20px;font-size:13px;font-weight:400}

/* header */
.site-header{position:absolute;left:0;top:0;width:1200px;height:75px;background:var(--white)}
.brand{position:absolute;left:60px;top:24px;font-family:"Cinzel",serif;font-size:19px;font-weight:500;color:var(--ink);letter-spacing:1px;display:flex;align-items:center;gap:8px;white-space:nowrap}
.brand-dot{flex:none;width:12px;height:12px;border-radius:50%;background:var(--gold)}
.nav a{position:absolute;top:29px;font-size:14px;color:var(--ink);text-decoration:none}
.nav a.active{color:var(--gold)}
.nav a.active::after{content:"";position:absolute;left:-4px;right:-4px;top:26px;height:1px;background:var(--gold)}

/* hero */
.hero-photo{position:absolute;left:0;top:75px;width:1200px;height:576px;background:linear-gradient(90deg,#e6e8ea 0%,#dcdfe1 45%,#cfd2d3 100%)}
.hero-title{position:absolute;left:60px;top:176px;font-size:55px;line-height:64px;color:var(--ink);letter-spacing:2px;font-family:"Cinzel",serif}
.hero-sub{position:absolute;left:62px;top:377px;font-size:14px;color:var(--ink)}
.contact-bar{position:absolute;left:149px;top:615px;width:901px;height:75px;border-radius:38px;overflow:hidden;display:flex}
.contact-bar .left{width:451px;background:var(--gold)}
.contact-bar .right{width:450px;background:#3b3a40}
.bar-item{position:absolute;top:640px;display:flex;align-items:center;gap:16px;color:var(--white);font-size:17px;white-space:nowrap}
.bar-circle{position:absolute;left:563px;top:615px;width:75px;height:75px;border-radius:50%;background:var(--white);border:4px solid var(--gold)}

/* sections */
.divider{position:absolute;height:1px;background:var(--gold)}
.section-title{position:absolute;left:0;width:1200px;text-align:center;font-family:"Cinzel",serif;font-size:27px;color:var(--ink);letter-spacing:1px;white-space:nowrap}
.section-copy{position:absolute;text-align:center;font-size:13.5px;line-height:22.5px;color:var(--text)}

/* services */
.service-photo{position:absolute;width:540px;height:375px}
.service-panel{position:absolute;width:540px;height:375px;background:var(--panel)}
.service-name{position:absolute;font-family:"Cinzel",serif;font-size:18px;color:var(--ink);letter-spacing:.5px}
.service-copy{position:absolute;width:480px;font-size:13.5px;line-height:22.5px;color:var(--text)}

/* news */
.news-card{position:absolute;top:2631px;width:340px;height:408px;background:var(--panel)}
.news-photo{position:absolute;left:0;top:0;width:340px;height:224px}
.news-meta{position:absolute;left:18px;top:241px;display:flex;align-items:center;gap:8px;font-size:13px;color:var(--text)}
.news-meta .gap{width:24px}
.news-title{position:absolute;left:20px;top:270px;width:300px;font-family:"Cinzel",serif;font-size:17px;font-weight:500;line-height:24px;color:var(--ink);letter-spacing:.5px}
.news-copy{position:absolute;left:20px;top:324px;width:290px;font-size:13px;line-height:22px;color:var(--text)}
.news-link{position:absolute;left:20px;top:372px;font-size:13.5px;color:var(--gold)}

/* footer */
.site-footer{position:absolute;left:0;top:3122px;width:1200px;height:262px;background:var(--ink)}
.foot-brand{position:absolute;left:60px;top:3200px;width:240px;font-family:"Cinzel",serif;font-size:26px;line-height:34px;color:var(--white);letter-spacing:1px;display:flex;align-items:center;gap:10px}
.foot-head{position:absolute;top:3176px;font-family:"Cinzel",serif;font-size:13px;color:var(--gold);letter-spacing:.5px;white-space:nowrap}
.foot-links{position:absolute;left:343px;top:3206px;list-style:none}
.foot-links li{height:28.5px;font-size:12.5px;color:var(--white);display:flex;align-items:center;gap:14px}
.foot-links li::before{content:"";width:5px;height:5px;border-radius:50%;background:var(--gold)}
.foot-contact{position:absolute;left:611px;display:flex;align-items:center;gap:10px;font-size:12.5px;color:var(--white);white-space:nowrap}
.email-field{position:absolute;left:889px;top:3211px;width:250px;height:33px;border-radius:17px;background:var(--white);font-size:12px;color:var(--muted);padding:9px 14px}
.copyright{position:absolute;left:0;top:3384px;width:1200px;height:40px;background:var(--gold);color:var(--white);font-size:12.5px;display:flex;align-items:center;justify-content:center}
</style>
</head>
<body>

<header class="site-header">
  <div class="brand"><span class="brand-dot"></span>Northfield Ledger Co.</div>
  <nav class="nav">
    <a class="active" style="left:401px">Home</a>
    <a style="left:484px">About</a>
    <a style="left:567px">Services</a>
    <a style="left:664px">News</a>
    <a style="left:743px">Contact</a>
  </nav>
  <div class="btn" style="left:1015px;top:19px;width:124px;height:37px;font-size:14px">Get Strated</div>
</header>

<section class="hero">
  <div class="hero-photo" role="img" aria-label="Smiling accountant with glasses writing in a notebook at a bright desk beside a laptop and a potted plant"></div>
  <h1 class="hero-title">Accounting and<br>Bookkeeping<br>Services</h1>
  <p class="hero-sub">Just A Click Away...</p>
  <div class="btn" style="left:60px;top:444px;width:146px;height:35px;font-size:14px">Request A Quote</div>
</section>

<div class="contact-bar"><div class="left"></div><div class="right"></div></div>
<div class="bar-circle" role="img" aria-label="Support team illustration"></div>
<div class="bar-item" style="left:214px">
  <svg width="30" height="30" viewBox="0 0 24 24" fill="none" stroke="#fff" stroke-width="1.3"><path d="M5 3h4l2 5-2.5 1.5a11 11 0 0 0 6 6L16 13l5 2v4a2 2 0 0 1-2 2A16 16 0 0 1 3 5a2 2 0 0 1 2-2z"/><path d="M14 3a7 7 0 0 1 7 7M14 6.5a3.5 3.5 0 0 1 3.5 3.5"/></svg>
  <span>Call Us Today!: <b style="font-weight:600">123 456 7890</b></span>
</div>
<div class="bar-item" style="left:692px">
  <svg width="36" height="26" viewBox="0 0 36 26" fill="none" stroke="#fff" stroke-width="1.6"><rect x="1" y="1" width="34" height="24" rx="1"/><path d="M1 1l17 14L35 1M1 25l12-12M35 25L23 13"/></svg>
  <span>info@northfieldledger.com</span>
</div>

<section class="welcome">
  <div class="divider" style="left:497px;top:808px;width:206px"></div>
  <h2 class="section-title" style="top:824px">Welcome to Accounting Northfield Ledger</h2>
  <p class="section-copy" style="left:262px;top:864px;width:676px">Lorem Ipsum is simply dummy text of the printing and typesetting industry. Lorem Ipsum has been the industry's standard dummy text ever since the 1500s, when an unknown printer took a galley of type and scrambled it to make a type specimen book. It has survived not only five centuries, but also the leap into electronic typesetting, remaining essentially unchanged. It was popularised in the 1960s with the release of Linotext sheets containing Lorem Ipsum passages, and more recently with desktop publishing software like Pagecraft Studio including versions of Lorem Ipsum.</p>
  <div class="btn" style="left:541px;top:1035px;width:117px;height:35px">Read More</div>
</section>

<section class="services">
  <div class="divider" style="left:477px;top:1200px;width:246px"></div>
  <h2 class="section-title" style="top:1210px">Our Services</h2>
  <p class="section-copy" style="left:262px;top:1248px;width:676px">Lorem Ipsum is simply dummy text of the printing and typesetting industry. Lorem Ipsum has been the industry's standard dummy text.</p>

  <div class="service-photo" style="left:60px;top:1320px;background:linear-gradient(135deg,#e9edf3,#c7d2e2)" role="img" aria-label="Two colleagues reviewing paperwork with a calculator at an office desk"></div>
  <div class="service-panel" style="left:600px;top:1320px"></div>
  <svg class="abs" style="left:638px;top:1372px" width="54" height="56" viewBox="0 0 54 56" fill="none" stroke="#e8a21c" stroke-width="1.8"><rect x="2" y="2" width="24" height="34" rx="2"/><rect x="6" y="6" width="16" height="7"/><path d="M7 19h3M13 19h3M19 19h3M7 25h3M13 25h3M19 25h3M7 31h3M13 31h3"/><path d="M26 14h16l8 8v32H22V40"/><path d="M30 30h14M30 36h14M30 42h14M30 48h14"/><circle cx="24" cy="46" r="7"/></svg>
  <h3 class="service-name" style="left:638px;top:1437px">Accounting</h3>
  <p class="service-copy" style="left:638px;top:1468px">Lorem Ipsum is simply dummy text of the printing and typesetting industry. Lorem Ipsum has been the industry's standard dummy text ever since the 1500s, when an unknown printer took a galley of type and scrambled it to make a type specimen book. It has survived not only five centuries, but also the leap into electronic typesetting.</p>
  <div class="btn" style="left:638px;top:1606px;width:116px;height:37px">Read More</div>

  <div class="service-panel" style="left:60px;top:1695px"></div>
  <svg class="abs" style="left:91px;top:1747px" width="56" height="56" viewBox="0 0 56 56" fill="none" stroke="#e8a21c" stroke-width="1.8"><rect x="6" y="2" width="30" height="46" rx="3"/><path d="M2 10h8M2 20h8M2 30h8M2 40h8"/><rect x="24" y="18" width="28" height="36" rx="3"/><rect x="28" y="22" width="20" height="8"/><path d="M30 36h3M37 36h3M44 36h3M30 42h3M37 42h3M44 42h3M30 48h3M37 48h3M44 48h3"/></svg>
  <h3 class="service-name" style="left:92px;top:1812px">Bookkeeping</h3>
  <p class="service-copy" style="left:92px;top:1843px">Lorem Ipsum is simply dummy text of the printing and typesetting industry. Lorem Ipsum has been the industry's standard dummy text ever since the 1500s, when an unknown printer took a galley of type and scrambled it to make a type specimen book. It has survived not only five centuries, but also the leap into electronic typesetting.</p>
  <div class="btn" style="left:91px;top:1981px;width:116px;height:37px">Read More</div>
  <div class="service-photo" style="left:600px;top:1695px;background:linear-gradient(90deg,#f5f5f3,#e2ddd6)" role="img" aria-label="Woman using a calculator at a round desk in front of a laptop"></div>

  <div class="service-photo" style="left:60px;top:2069px;background:linear-gradient(135deg,#d9c29a,#9a9ca3)" role="img" aria-label="Hands typing on a calculator beside a laptop, coins and financial charts"></div>
  <div class="service-panel" style="left:600px;top:2069px"></div>
  <svg class="abs" style="left:638px;top:2122px" width="56" height="56" viewBox="0 0 56 56" fill="none" stroke="#e8a21c" stroke-width="1.8"><path d="M4 2h30l8 8v42H4z"/><text x="8" y="22" font-family="Poppins,sans-serif" font-size="13" fill="#e8a21c" stroke="none">TAX</text><path d="M8 30h14M8 36h14M8 42h14"/><rect x="28" y="26" width="24" height="28" rx="2"/><path d="M32 32h16M32 38h3M38 38h3M44 38h3M32 44h3M38 44h3M44 44h3"/></svg>
  <h3 class="service-name" style="left:639px;top:2186px">Tax Prep</h3>
  <p class="service-copy" style="left:639px;top:2218px">Lorem Ipsum is simply dummy text of the printing and typesetting industry. Lorem Ipsum has been the industry's standard dummy text ever since the 1500s, when an unknown printer took a galley of type and scrambled it to make a type specimen book. It has survived not only five centuries, but also the leap into electronic typesetting.</p>
  <div class="btn" style="left:639px;top:2356px;width:116px;height:37px">Read More</div>
</section>

<section class="news">
  <div class="divider" style="left:497px;top:2565px;width:206px"></div>
  <h2 class="section-title" style="top:2577px">Our Latest News</h2>

  <article class="news-card" style="left:60px">
    <div class="news-photo" style="background:linear-gradient(135deg,#e9eef2,#8d9aa6)" role="img" aria-label="Team members reviewing charts and devices on a white table, seen from above"></div>
    <div class="news-meta">
      <svg width="18" height="18" viewBox="0 0 18 18" fill="none" stroke="#333" stroke-width="1.2"><rect x="1.5" y="3" width="15" height="13.5"/><path d="M1.5 7h15M5 1v4M13 1v4M5 10h2M8 10h2M11 10h2M5 13h2M8 13h2M11 13h2"/></svg>
      <span>15, Aug 2022</span><span class="gap"></span>
      <svg width="22" height="18" viewBox="0 0 22 18" fill="none" stroke="#333" stroke-width="1.2"><ellipse cx="11" cy="8" rx="9" ry="6.5"/><path d="M5 13l-2 4 5-2.5"/><path d="M7 8h8"/></svg>
      <span>155</span>
    </div>
    <h3 class="news-title">Lorem Ipsum is simply dummy text.</h3>
    <p class="news-copy">Lorem Ipsum is simply dummy text of the printing and typesetting industry.</p>
    <span class="news-link">Read More</span>
  </article>

  <article class="news-card" style="left:428px">
    <div class="news-photo" style="background:linear-gradient(135deg,#f3f4f6,#b9bfc7)" role="img" aria-label="Businesswoman smiling at her desk in an open office"></div>
    <div class="news-meta">
      <svg width="18" height="18" viewBox="0 0 18 18" fill="none" stroke="#333" stroke-width="1.2"><rect x="1.5" y="3" width="15" height="13.5"/><path d="M1.5 7h15M5 1v4M13 1v4M5 10h2M8 10h2M11 10h2M5 13h2M8 13h2M11 13h2"/></svg>
      <span>15, Aug 2022</span><span class="gap"></span>
      <svg width="22" height="18" viewBox="0 0 22 18" fill="none" stroke="#333" stroke-width="1.2"><ellipse cx="11" cy="8" rx="9" ry="6.5"/><path d="M5 13l-2 4 5-2.5"/><path d="M7 8h8"/></svg>
      <span>155</span>
    </div>
    <h3 class="news-title">Lorem Ipsum is simply dummy text.</h3>
    <p class="news-copy">Lorem Ipsum is simply dummy text of the printing and typesetting industry.</p>
    <span class="news-link">Read More</span>
  </article>

  <article class="news-card" style="left:799px">
    <div class="news-photo" style="background:linear-gradient(135deg,#3a3c40,#c9ccd1)" role="img" aria-label="Hands working with a calculator, laptop and printed charts on a desk"></div>
    <div class="news-meta">
      <svg width="18" height="18" viewBox="0 0 18 18" fill="none" stroke="#333" stroke-width="1.2"><rect x="1.5" y="3" width="15" height="13.5"/><path d="M1.5 7h15M5 1v4M13 1v4M5 10h2M8 10h2M11 10h2M5 13h2M8 13h2M11 13h2"/></svg>
      <span>15, Aug 2022</span><span class="gap"></span>
      <svg width="22" height="18" viewBox="0 0 22 18" fill="none" stroke="#333" stroke-width="1.2"><ellipse cx="11" cy="8" rx="9" ry="6.5"/><path d="M5 13l-2 4 5-2.5"/><path d="M7 8h8"/></svg>
      <span>155</span>
    </div>
    <h3 class="news-title">Lorem Ipsum is simply dummy text.</h3>
    <p class="news-copy">Lorem Ipsum is simply dummy text of the printing and typesetting industry.</p>
    <span class="news-link">Read More</span>
  </article>
</section>

<footer>
  <div class="site-footer"></div>
  <div class="foot-brand"><span class="brand-dot" style="width:14px;height:14px"></span><span>Northfield Ledger Co.</span></div>

  <h4 class="foot-head" style="left:339px">Quick Links</h4>
  <ul class="foot-links">
    <li>Home</li><li>About Us</li><li>Services</li><li>News</li><li>Contact Us</li>
  </ul>

  <h4 class="foot-head" style="left:613px">Contact Us</h4>
  <div class="foot-contact" style="top:3208px">
    <svg width="16" height="18" viewBox="0 0 16 18" fill="none" stroke="#e8a21c" stroke-width="1.3"><path d="M8 17s6-6 6-10A6 6 0 0 0 2 7c0 4 6 10 6 10z"/><circle cx="8" cy="7" r="2.2"/><path d="M3 17h10"/></svg>
    <span>123 , Lorem ipsum is a dummy text.</span>
  </div>
  <div class="foot-contact" style="top:3246px">
    <svg width="18" height="18" viewBox="0 0 24 24" fill="none" stroke="#e8a21c" stroke-width="1.5"><path d="M5 3h4l2 5-2.5 1.5a11 11 0 0 0 6 6L16 13l5 2v4a2 2 0 0 1-2 2A16 16 0 0 1 3 5a2 2 0 0 1 2-2z"/></svg>
    <span style="font-weight:500">123 456 7890</span>
  </div>
  <div class="foot-contact" style="top:3285px">
    <svg width="22" height="16" viewBox="0 0 22 16" fill="none" stroke="#e8a21c" stroke-width="1.4"><rect x="1" y="1" width="20" height="14"/><path d="M1 1l10 8 10-8"/></svg>
    <span>info@northfieldledger.com</span>
  </div>

  <h4 class="foot-head" style="left:890px">Subscribe To Our Newslatter</h4>
  <div class="email-field">E-mail*</div>
  <div class="btn" style="left:889px;top:3260px;width:89px;height:33px;font-size:12px">Subscribe</div>

  <div class="copyright">Copyright © 2022&nbsp;<b style="font-weight:600">NORTHFIELD LEDGER CO.</b>&nbsp;All rights reserved.</div>
</footer>

</body>
</html>
```